Homepage Redesign - Hi-tech business Law Firm

I'm looking for an updated graphic design (pdf file) for the homepage of dorvantlegal.ca (and which will form the general template of the other pages - but you don't need to design that). Detailed specs are in the Word file.

Deliverable is 1 pdf file that I find good looking, that sets forth the layout of the new page.

Target Market(s)

Sophisticated customers

Industry/Entity Type

Legal

Number of Pages Required

1 page

Requirements
Nice to have
• For a main background, tech type images to do with high powered boardrooms, computers, graphs, numbers, high tech manufacturing lines etc. Also, I tend to like blues and light greys, and uploaded a file today that shows my generally preferred layout, which a few of you have been getting close to.
Should not have
• Any mention of 'Personal Injury,' backgrounds that include books, or buildings with roman columns. Page should not be in dark colors or harsh on the eyes.

```html
<!DOCTYPE html>
<html lang="en">
<head>
<meta charset="utf-8">
<title>Dorvant Legal — Homepage Hero Options</title>
<link rel="stylesheet" href="https://fonts.googleapis.com/css2?family=Playfair+Display:wght@400;500&family=Poppins:wght@400;500;600&display=swap">
<style>
  :root {
    --page: #ffffff;
    --navy: #16334d;
    --ink: #1d1f22;
    --blue-accent: #2f6f9a;
    --button-blue: #2d6e93;
    --grey-light-1: #eef0f2;
    --grey-light-2: #c9cdd2;
    --grey-dark-1: #4c535b;
    --grey-dark-2: #7a828b;
    --pale-1: #f4f7f9;
    --pale-2: #e8eef2;
    --frame: #8d939a;
    --white: #ffffff;
    --suit-1: #2a3442;
    --suit-2: #5d6a7a;
  }
  * { box-sizing: border-box; margin: 0; padding: 0; }
  html, body { width: 1200px; height: 3492px; overflow: hidden; background: var(--page); }
  body { position: relative; font-family: "Poppins", sans-serif; }

  .hero { position: absolute; left: 0; width: 1200px; overflow: hidden; }
  .hero__backdrop { position: absolute; inset: 0; }
  .hero__portrait {
    position: absolute; bottom: 0;
    border-radius: 170px 170px 0 0;
    background: linear-gradient(180deg, var(--suit-2) 0%, var(--suit-1) 45%, #1c232e 100%);
  }
  .hero__title {
    position: absolute; font-family: "Playfair Display", serif; font-weight: 400;
    line-height: 1; letter-spacing: 0.5px; white-space: nowrap;
  }
  .hero__title--accent { color: var(--navy); }
  .hero__title--dark { color: var(--ink); }
  .hero__tagline { position: absolute; font-size: 17px; line-height: 1.5; color: #3a3f45; }
  .hero__button {
    position: absolute; height: 44px; display: flex; align-items: center; justify-content: center; gap: 10px;
    font-size: 13px; font-weight: 600; letter-spacing: 1.5px; color: var(--white); background: var(--navy);
  }
  .hero__button svg { width: 26px; height: 12px; }

  /* Option 1 */
  .hero--framed { top: 72px; height: 608px; }
  .hero--framed .hero__backdrop { background: linear-gradient(180deg, #f6f7f8 0%, var(--grey-light-1) 55%, var(--grey-light-2) 100%); }
  .hero__frame { position: absolute; left: 120px; top: 56px; width: 968px; height: 480px; border: 2px solid var(--frame); }

  /* Option 2 */
  .hero--dark { top: 740px; height: 660px; }
  .hero--dark .hero__backdrop { background: linear-gradient(180deg, var(--grey-dark-2) 0%, var(--grey-dark-1) 100%); }
  .hero--dark .hero__title, .hero--dark .hero__tagline { color: var(--white); }

  /* Option 3 */
  .hero--light { top: 1460px; height: 600px; }
  .hero--light .hero__backdrop { background: linear-gradient(180deg, #f3f4f5 0%, #dfe2e5 70%, #cfd3d7 100%); }

  /* Option 4 */
  .hero--bracket { top: 2108px; height: 612px; }
  .hero--bracket .hero__backdrop { background: linear-gradient(135deg, var(--pale-1) 0%, var(--pale-2) 100%); }
  .hero__bracket { position: absolute; left: 128px; top: 92px; width: 64px; height: 300px;
    border-left: 3px solid var(--navy); border-top: 3px solid var(--navy); border-bottom: 3px solid var(--navy); }
  .hero--bracket .hero__subtitle { position: absolute; font-family: "Playfair Display", serif; font-size: 36px; line-height: 1.2; color: var(--navy); white-space: nowrap; }
  .hero__subtitle em { font-style: normal; color: var(--blue-accent); }
  .hero--bracket .hero__button { background: var(--button-blue); }

  /* Option 5 */
  .hero--clean { top: 2752px; height: 640px; border-top: 1px solid #ececec; }
  .hero--clean .hero__backdrop { background: var(--white); }
  .hero__rule { position: absolute; left: 120px; top: 200px; width: 540px; height: 1px; background: var(--grey-light-2); }
</style>
</head>
<body>

<section class="hero hero--framed">
  <div class="hero__backdrop" role="img" aria-label="Soft grey city skyline along the waterfront"></div>
  <div class="hero__frame"></div>
  <h1 class="hero__title hero__title--accent" style="left:192px; top:110px; font-size:76px;">Experience</h1>
  <h2 class="hero__title hero__title--dark" style="left:192px; top:200px; font-size:76px;">Matters</h2>
  <p class="hero__tagline" style="left:194px; top:306px; width:380px;">Winning. My clients depend on me for it. Shouldn't you?</p>
  <a class="hero__button" style="left:194px; top:382px; width:184px;">LEARN MORE
    <svg viewBox="0 0 26 12"><path d="M0 6h23M18 1l6 5-6 5" fill="none" stroke="#fff" stroke-width="1.6"/></svg></a>
  <div class="hero__portrait" role="img" aria-label="Portrait of the lead lawyer in a dark suit and blue shirt" style="left:620px; width:440px; bottom:72px; height:520px;"></div>
</section>

<section class="hero hero--dark">
  <div class="hero__backdrop" role="img" aria-label="Muted grey city skyline with a tall tower"></div>
  <h1 class="hero__title" style="left:152px; top:166px; font-size:76px;">Experience</h1>
  <h2 class="hero__title" style="left:152px; top:256px; font-size:76px;">Matters</h2>
  <p class="hero__tagline" style="left:154px; top:362px; width:360px;">Winning. My clients depend on me for it. Shouldn't you?</p>
  <a class="hero__button" style="left:154px; top:438px; width:184px;">LEARN MORE
    <svg viewBox="0 0 26 12"><path d="M0 6h23M18 1l6 5-6 5" fill="none" stroke="#fff" stroke-width="1.6"/></svg></a>
  <div class="hero__portrait" role="img" aria-label="Portrait of the lead lawyer in a dark suit and blue shirt" style="left:600px; width:460px; height:600px;"></div>
</section>

<section class="hero hero--light">
  <div class="hero__backdrop" role="img" aria-label="Pale grey city skyline with stadium and tower"></div>
  <h1 class="hero__title hero__title--accent" style="left:184px; top:140px; font-size:72px;">Experience</h1>
  <h2 class="hero__title hero__title--dark" style="left:184px; top:226px; font-size:72px;">Matters</h2>
  <p class="hero__tagline" style="left:186px; top:326px; width:360px;">Winning. My clients depend on me for it. Shouldn't you?</p>
  <a class="hero__button" style="left:186px; top:400px; width:184px;">LEARN MORE
    <svg viewBox="0 0 26 12"><path d="M0 6h23M18 1l6 5-6 5" fill="none" stroke="#fff" stroke-width="1.6"/></svg></a>
  <div class="hero__portrait" role="img" aria-label="Portrait of the lead lawyer in a dark suit and blue shirt" style="left:620px; width:460px; height:560px;"></div>
</section>

<section class="hero hero--bracket">
  <div class="hero__backdrop" role="img" aria-label="Light blue-grey background with faint geometric line network"></div>
  <div class="hero__bracket"></div>
  <h1 class="hero__title hero__title--dark" style="left:160px; top:140px; font-size:56px;">Winning Matters</h1>
  <p class="hero__subtitle" style="left:162px; top:212px;">My clients <em>depend</em><br>on me for it. Shouldn't you?</p>
  <a class="hero__button" style="left:166px; top:336px; width:208px;">LEARN MORE</a>
  <div class="hero__portrait" role="img" aria-label="Portrait of the lead lawyer in a dark suit and light blue shirt" style="left:660px; width:360px; bottom:24px; height:560px;"></div>
</section>

<section class="hero hero--clean">
  <div class="hero__backdrop"></div>
  <h1 class="hero__title hero__title--accent" style="left:120px; top:100px; font-size:80px; letter-spacing:3px;">Experience</h1>
  <div class="hero__rule"></div>
  <h2 class="hero__title hero__title--dark" style="left:120px; top:214px; font-size:76px; letter-spacing:3px;">Matters</h2>
  <p class="hero__tagline" style="left:122px; top:326px; width:400px;">Winning. My clients depend on me for it. Shouldn't you?</p>
  <a class="hero__button" style="left:122px; top:412px; width:208px;">LEARN MORE</a>
  <div class="hero__portrait" role="img" aria-label="Portrait of the lead lawyer in a dark suit and blue tie" style="left:660px; width:360px; bottom:24px; height:600px;"></div>
</section>

</body>
</html>
```